Solace Chiropractic & Acupuncture Business Cards

I need a business card design that feels elevated. I am open to any of the logo designs uploaded. We have two doctors so I'll need to be able to change out the names.

Information:
Marnie Toller D.C., M.S. Ac. NCA
584 W 12th St, Ste 320
Linden Falls, KS 67419
solacegrove.net
620-555-0147
drmarnie@solacegrove.com
Updates

We have designs we like now, we are just trying to choose between top contenders. Thanks for your submissions!

Contact Information for Business Card

noted in description

Requirements
Must have
• ability to edit info if possible
Nice to have
• Please see our website solacegrove.net for our style and colors

```html
<!DOCTYPE html>
<html lang="en">
<head>
<meta charset="utf-8">
<title>Solace Chiropractic &amp; Acupuncture – Business Cards</title>
<link href="https://fonts.googleapis.com/css2?family=Bellefair&family=Poppins:wght@400&display=swap" rel="stylesheet">
<style>
  :root {
    --backdrop: #c3bcb1;
    --card: #e6e2dc;
    --navy: #36475d;
    --icon-grey: #a9a9a9;
    --rule-grey: #b3b0ab;
    --ring: #e6e2dc;
  }
  html, body {
    margin: 0;
    padding: 0;
    width: 1200px;
    height: 1200px;
    overflow: hidden;
    background: var(--backdrop);
  }
  .card {
    position: absolute;
    left: 319px;
    width: 562px;
    height: 337px;
    background: var(--card);
    overflow: hidden;
  }
  .card--front { top: 272px; }
  .card--back { top: 629px; }

  /* Front */
  .wordmark {
    position: absolute;
    left: 0;
    right: 0;
    top: 97px;
    text-align: center;
    font-family: "Bellefair", serif;
    color: var(--navy);
  }
  .wordmark__name {
    display: block;
    font-size: 118px;
    line-height: 1;
  }
  .wordmark__tagline {
    display: block;
    margin-top: 3px;
    font-size: 17px;
    letter-spacing: 0.5px;
    line-height: 1;
  }

  /* Back */
  .back__panel {
    position: absolute;
    left: 0;
    top: 0;
    width: 562px;
    height: 337px;
  }
  .badge {
    position: absolute;
    left: 26px;
    top: 94px;
    width: 150px;
    height: 150px;
    border: 1px solid var(--ring);
    border-radius: 50%;
    display: flex;
    align-items: center;
    justify-content: center;
    font-family: "Bellefair", serif;
    font-size: 34px;
    color: var(--ring);
  }
  .doctor {
    position: absolute;
    left: 229px;
    top: 42px;
    font-family: "Bellefair", serif;
    color: var(--navy);
  }
  .doctor__name {
    font-size: 47px;
    line-height: 1;
    margin: 0;
    font-weight: 400;
  }
  .doctor__credentials {
    font-size: 21px;
    line-height: 1;
    margin: 4px 0 0 0;
    letter-spacing: 0.6px;
    opacity: 0.85;
  }
  .divider {
    position: absolute;
    left: 209px;
    top: 124px;
    width: 309px;
    height: 1px;
    background: var(--rule-grey);
  }
  .contact {
    position: absolute;
    left: 229px;
    margin: 0;
    padding: 0;
    list-style: none;
    font-family: "Poppins", sans-serif;
    color: var(--navy);
  }
  .contact__item {
    position: absolute;
    left: 0;
    display: flex;
    align-items: flex-start;
    white-space: nowrap;
  }
  .contact__icon {
    width: 24px;
    height: 24px;
    margin-right: 19px;
    flex: none;
  }
  .contact__text {
    font-size: 16.5px;
    line-height: 29px;
  }
  .contact__item--address { top: 140px; }
  .contact__item--web { top: 203px; }
  .contact__item--phone { top: 244px; }
  .contact__item--phone .contact__text { font-size: 19px; letter-spacing: 0.6px; }
  .contact__item--email { top: 287px; }
</style>
</head>
<body>

<section class="card card--front" aria-label="Card front">
  <div class="wordmark">
    <span class="wordmark__name">Solace</span>
    <span class="wordmark__tagline">CHIROPRACTIC &amp; ACUPUNCTURE</span>
  </div>
</section>

<section class="card card--back" aria-label="Card back">
  <svg class="back__panel" viewBox="0 0 562 337" aria-hidden="true">
    <path d="M0 0 H174 C164 50 178 100 196 150 C216 205 222 270 174 337 H0 Z" fill="var(--navy)"/>
  </svg>

  <div class="badge">Solace</div>

  <div class="doctor">
    <h1 class="doctor__name">Marnie Toller</h1>
    <p class="doctor__credentials">D.C., M.S. Ac. NCA</p>
  </div>

  <div class="divider"></div>

  <ul class="contact">
    <li class="contact__item contact__item--address">
      <svg class="contact__icon" viewBox="0 0 24 24" aria-hidden="true">
        <path d="M12 2a8 8 0 0 0-8 8c0 5 8 12.5 8 12.5S20 15 20 10a8 8 0 0 0-8-8zm0 11.5a3.5 3.5 0 1 1 0-7 3.5 3.5 0 0 1 0 7z" fill="var(--icon-grey)"/>
      </svg>
      <span class="contact__text">584 W 12th St, Ste 320<br>Linden Falls, KS 67419</span>
    </li>
    <li class="contact__item contact__item--web">
      <svg class="contact__icon" viewBox="0 0 24 24" aria-hidden="true" fill="none" stroke="var(--icon-grey)" stroke-width="1.5">
        <circle cx="12" cy="12" r="10"/>
        <ellipse cx="12" cy="12" rx="4.5" ry="10"/>
        <path d="M2 12h20M4 6.5h16M4 17.5h16"/>
      </svg>
      <span class="contact__text">solacegrove.net</span>
    </li>
    <li class="contact__item contact__item--phone">
      <svg class="contact__icon" viewBox="0 0 24 24" aria-hidden="true">
        <path d="M6.6 2.5l2.6 3.9c.4.6.3 1.3-.2 1.8L7.6 9.6c1.2 2.7 3.5 5 6.2 6.3l1.4-1.4c.5-.5 1.2-.6 1.8-.2l3.9 2.6c.6.4.8 1.2.4 1.8l-1.2 2c-.6 1-1.8 1.4-2.9 1.1C10.3 19.8 4.4 13.9 2.6 7c-.3-1.1.2-2.300 1.1-2.9l2-1.2c.6-.4 1.4-.2 1.8.4z" fill="var(--icon-grey)"/>
      </svg>
      <span class="contact__text">620-555-0147</span>
    </li>
    <li class="contact__item contact__item--email">
      <svg class="contact__icon" viewBox="0 0 24 24" aria-hidden="true">
        <rect x="1" y="5" width="22" height="15" fill="var(--icon-grey)"/>
        <path d="M1 5l11 8 11-8M1 20l8-7M23 20l-8-7" fill="none" stroke="var(--card)" stroke-width="1.3"/>
      </svg>
      <span class="contact__text">drmarnie@solacegrove.com</span>
    </li>
  </ul>
</section>

</body>
</html>
```